Amber Hollow Productions

I need a business card design for a new freelance film production company using or incorporating the logo:
I want the card to be creative, minimal, yet professional. Feel free to use a variety of different shapes and sizes/ textures for the card.

Industry/Entity Type

Film Production

```html
<!DOCTYPE html>
<html lang="en">
<head>
<meta charset="utf-8">
<title>Amber Hollow Productions – Business Cards</title>
<link rel="stylesheet" href="https://fonts.googleapis.com/css2?family=Raleway:wght@400&display=swap">
<style>
  :root {
    --page-bg: #ffffff;
    --card-grey: #c3c4c6;
    --brand-blue: #2a5cb0;
    --purple-deep: #4a2a7a;
    --purple-mid: #5b3a90;
    --purple-soft: #8a76b4;
    --purple-pale: #b0a6cc;
    --text-light: #ffffff;
    --text-muted: #8d8e91;
  }
  * { margin: 0; padding: 0; box-sizing: border-box; }
  html, body {
    width: 1200px;
    height: 874px;
    overflow: hidden;
    background: var(--page-bg);
    font-family: "Raleway", sans-serif;
  }
  .canvas {
    position: relative;
    width: 1200px;
    height: 874px;
  }
  .card {
    position: absolute;
    background: var(--card-grey);
    overflow: hidden;
  }
  .card-front {
    left: 16px;
    top: 86px;
    width: 747px;
    height: 408px;
    z-index: 2;
  }
  .card-back {
    left: 396px;
    top: 420px;
    width: 730px;
    height: 390px;
    z-index: 1;
  }
  .front-shapes {
    position: absolute;
    inset: 0;
    width: 100%;
    height: 100%;
  }
  .front-brand {
    position: absolute;
    left: 58px;
    top: 352px;
    display: flex;
    align-items: center;
    gap: 10px;
    color: var(--brand-blue);
    font-size: 20px;
    font-weight: 400;
    letter-spacing: 1px;
    line-height: 1;
  }
  .brand-square {
    width: 18px;
    height: 18px;
    background: var(--brand-blue);
  }
  .front-info {
    position: absolute;
    left: 422px;
    top: 270px;
    color: var(--text-light);
    font-size: 28px;
    font-weight: 400;
    line-height: 1.2;
  }
  .back-brand {
    position: absolute;
    left: 0;
    right: 0;
    top: 156px;
    text-align: center;
  }
  .back-name {
    color: var(--brand-blue);
    font-size: 58px;
    font-weight: 400;
    letter-spacing: 3px;
    line-height: 1;
  }
  .back-tagline {
    margin-top: 20px;
    color: var(--text-muted);
    font-size: 17px;
    font-weight: 400;
    letter-spacing: 33px;
    padding-left: 33px;
    line-height: 1;
  }
</style>
</head>
<body>
  <main class="canvas">
    <section class="card card-front" aria-label="Business card front">
      <svg class="front-shapes" viewBox="0 0 747 408" aria-hidden="true">
        <defs>
          <linearGradient id="panel-purple" x1="0" y1="0" x2="1" y2="0">
            <stop offset="0" stop-color="#5b3a90"/>
            <stop offset="1" stop-color="#4a2a7a"/>
          </linearGradient>
        </defs>
        <polygon class="stripe-pale" points="470,142 747,0 747,22" fill="var(--purple-pale)"/>
        <polygon class="stripe-soft" points="380,178 747,20 747,42" fill="var(--purple-soft)"/>
        <polygon class="info-panel" points="328,198 747,40 747,408 328,408" fill="url(#panel-purple)"/>
      </svg>
      <div class="front-brand">
        <span class="brand-square"></span>
        <span class="brand-name">AMBER HOLLOW</span>
      </div>
      <p class="front-info">information</p>
    </section>

    <section class="card card-back" aria-label="Business card back">
      <div class="back-brand">
        <h1 class="back-name">AMBER HOLLOW</h1>
        <p class="back-tagline">PRODUCTIONS</p>
      </div>
    </section>
  </main>
</body>
</html>
```